School teacher strategies for teachers to improve their lessons.

This is for displays for teachers in their office about how to best teach students. This should be styled in a professional way that aligns with the colour themes of the school.

For reference, here is the school's website:
https://tallowmeresc.qz.edu.au/

I have attached a previous document "Steady Habits" - please use similar theme.

Target Market(s)

teachers at this school

Colors

Requirements
Must have
• School logo. And aligned to previous designs

```html
<!DOCTYPE html>
<html lang="en">
<head>
<meta charset="utf-8">
<title>Write a Powerful Learning Goal &amp; Success Criteria</title>
<link rel="stylesheet" href="https://fonts.googleapis.com/css2?family=Montserrat:wght@400;500;600;700&display=swap">
<style>
  :root{
    --navy:#233c89;
    --navy-text:#25388a;
    --yellow:#f1e26a;
    --yellow-title:#f3e65a;
    --paper:#f8f8f8;
    --stage:#e8e9eb;
    --goal-grey:#d4cfd0;
    --shadow:#b9b4b6;
    --white:#ffffff;
  }
  *{box-sizing:border-box;margin:0;padding:0}
  html,body{width:1200px;height:967px;overflow:hidden}
  body{background:var(--stage);font-family:"Montserrat",Arial,sans-serif;position:relative}

  .poster{position:absolute;left:315px;top:80px;width:570px;height:806px;background:var(--paper);box-shadow:6px 8px 14px rgba(0,0,0,.18);overflow:hidden}

  .header-band{position:absolute;left:0;top:35px;width:570px;height:66px;background:var(--navy)}
  .school-mark{position:absolute;left:57px;top:8px;width:101px;height:118px;background:var(--white);border-radius:14px;box-shadow:0 2px 6px rgba(0,0,0,.15);display:flex;align-items:center;justify-content:center;text-align:center;color:var(--navy);font-weight:600;font-size:11px;line-height:1.35;letter-spacing:.3px}
  .title{position:absolute;left:187px;top:48px;color:var(--yellow-title);font-weight:600;font-size:17.5px;line-height:20px;letter-spacing:.2px}

  .essentials{position:absolute;left:35px;top:145px;width:500px;height:171px;background:var(--navy);border-radius:8px;box-shadow:0 2px 6px rgba(0,0,0,.15)}
  .essentials-tag{position:absolute;left:0;top:17px;width:146px;height:28px}
  .essentials-tag span{position:absolute;left:16px;top:3px;color:var(--navy);font-weight:600;font-size:16.5px;letter-spacing:.3px}
  .essential{position:absolute;color:var(--white);font-size:9.4px;line-height:10.6px}
  .essential h3{font-weight:600;font-size:9.6px;line-height:10.6px;letter-spacing:.1px}
  .essential b{font-weight:700}
  .essential .tick{position:absolute;left:-28px;top:0;width:19px;height:19px}
  .col-left{left:43px;width:230px}
  .col-right{left:285px;width:210px}

  .track{position:absolute;top:334px;width:242px;height:268px;border-radius:8px;box-shadow:0 2px 6px rgba(0,0,0,.15)}
  .track-curriculum{left:35px;background:var(--navy)}
  .track-behaviour{left:293px;background:var(--yellow)}
  .track h2{position:absolute;left:0;top:12px;width:100%;text-align:center;font-weight:600;font-size:17px;letter-spacing:.4px}
  .track-curriculum h2{color:var(--white)}
  .track-behaviour h2{color:var(--navy)}
  .card{position:absolute;left:17px;width:208px;height:65px;background:var(--paper);border-radius:7px;display:flex;flex-direction:column;justify-content:center;align-items:center;text-align:center;color:var(--navy-text);font-size:9.4px;line-height:10.6px;padding:0 8px}
  .card h4{font-weight:600;font-size:9.6px;line-height:10.6px}
  .card-what{top:38px}
  .card-how{top:112px}
  .card-why{top:186px}

  .goal-tab{position:absolute;left:225px;top:620px;width:120px;height:30px;background:var(--goal-grey);border-radius:8px 8px 0 0}
  .goal-band{position:absolute;left:0;top:638px;width:570px;height:168px;background:var(--goal-grey);border-radius:10px 10px 0 0}
  .goal-title{position:absolute;left:225px;top:627px;width:120px;text-align:center;color:var(--navy);font-weight:700;font-size:17px;letter-spacing:.3px}
  .step{position:absolute;width:144px;height:37px;background:var(--yellow);border-radius:7px;box-shadow:3px 3px 0 var(--shadow);display:flex;align-items:center;justify-content:center;text-align:center;color:var(--navy-text);font-weight:500;font-size:10.4px;line-height:12px;letter-spacing:.2px}
  .row-1{top:664px}
  .row-2{top:735px}
  .col-a{left:35px}
  .col-b{left:213px}
  .col-c{left:392px}
  .flow-arrows{position:absolute;left:0;top:638px;width:570px;height:168px}
</style>
</head>
<body>
<main class="poster">
  <div class="header-band"></div>
  <div class="school-mark">TALLOWMERE<br>STATE<br>COLLEGE</div>
  <h1 class="title">WRITE A POWERFUL LEARNING GOAL<br>&amp; SUCCESS CRITERIA</h1>

  <section class="essentials">
    <svg class="essentials-tag" viewBox="0 0 146 28" aria-hidden="true"><polygon points="0,0 146,0 134,14 146,28 0,28" fill="var(--yellow-title)"/></svg>
    <div class="essentials-tag"><span>ESSENTIALS</span></div>

    <div class="essential col-left" style="top:56px">
      <svg class="tick" viewBox="0 0 20 20"><circle cx="10" cy="10" r="8.5" fill="none" stroke="var(--yellow-title)" stroke-width="1.4"/><path d="M5.5 10.5l3 3 6-7" fill="none" stroke="var(--yellow-title)" stroke-width="1.8" stroke-linecap="round" stroke-linejoin="round"/></svg>
      <h3>ABOUT LEARNING, NOT TASKS</h3>
      <p>Focus on knowledge/skill students will<br>learn today.</p>
    </div>
    <div class="essential col-left" style="top:93px">
      <svg class="tick" viewBox="0 0 20 20"><circle cx="10" cy="10" r="8.5" fill="none" stroke="var(--yellow-title)" stroke-width="1.4"/><path d="M5.5 10.5l3 3 6-7" fill="none" stroke="var(--yellow-title)" stroke-width="1.8" stroke-linecap="round" stroke-linejoin="round"/></svg>
      <h3>RIGHT VERB, RIGHT LEVEL</h3>
      <p>Choose a precise Bloom's/cognitive verb.</p>
    </div>
    <div class="essential col-left" style="top:129px">
      <svg class="tick" viewBox="0 0 20 20"><circle cx="10" cy="10" r="8.5" fill="none" stroke="var(--yellow-title)" stroke-width="1.4"/><path d="M5.5 10.5l3 3 6-7" fill="none" stroke="var(--yellow-title)" stroke-width="1.8" stroke-linecap="round" stroke-linejoin="round"/></svg>
      <h3>ONE IDEA ONLY</h3>
      <p>Keep scope tight to manage cognitive<br>load.</p>
    </div>

    <div class="essential col-right" style="top:20px">
      <svg class="tick" viewBox="0 0 20 20"><circle cx="10" cy="10" r="8.5" fill="none" stroke="var(--yellow-title)" stroke-width="1.4"/><path d="M5.5 10.5l3 3 6-7" fill="none" stroke="var(--yellow-title)" stroke-width="1.8" stroke-linecap="round" stroke-linejoin="round"/></svg>
      <h3>STUDENT-FRIENDLY</h3>
      <p>plain language students can restate;<br><b>accessible</b> to all students.</p>
    </div>
    <div class="essential col-right" style="top:56px">
      <svg class="tick" viewBox="0 0 20 20"><circle cx="10" cy="10" r="8.5" fill="none" stroke="var(--yellow-title)" stroke-width="1.4"/><path d="M5.5 10.5l3 3 6-7" fill="none" stroke="var(--yellow-title)" stroke-width="1.8" stroke-linecap="round" stroke-linejoin="round"/></svg>
      <h3>VISIBLE &amp; REVISITED</h3>
      <p>Display it; say it at transitions and again<br>during the review at lesson end.</p>
    </div>
    <div class="essential col-right" style="top:93px">
      <svg class="tick" viewBox="0 0 20 20"><circle cx="10" cy="10" r="8.5" fill="none" stroke="var(--yellow-title)" stroke-width="1.4"/><path d="M5.5 10.5l3 3 6-7" fill="none" stroke="var(--yellow-title)" stroke-width="1.8" stroke-linecap="round" stroke-linejoin="round"/></svg>
      <h3>ASSESSABLE</h3>
      <p>Design quick checks and an exit slip that<br>align to the Success Criteria.</p>
    </div>
    <div class="essential col-right" style="top:129px">
      <svg class="tick" viewBox="0 0 20 20"><circle cx="10" cy="10" r="8.5" fill="none" stroke="var(--yellow-title)" stroke-width="1.4"/><path d="M5.5 10.5l3 3 6-7" fill="none" stroke="var(--yellow-title)" stroke-width="1.8" stroke-linecap="round" stroke-linejoin="round"/></svg>
      <h3>SAME LEARNING GOAL FOR ALL</h3>
      <p>Differentiate supports (scaffolds/groups),<br>not the intention.</p>
    </div>
  </section>

  <section class="track track-curriculum">
    <h2>CURRICULUM</h2>
    <div class="card card-what"><h4>WHAT</h4><p>The specific knowledge/skill linked to<br>today's learning goal.</p></div>
    <div class="card card-how"><h4>HOW</h4><p>The routine/strategy students will use<br>to demonstrate it (e.g., worked-example<br>steps, analysis routine, calculation<br>method).</p></div>
    <div class="card card-why"><h4>WHY</h4><p>The purpose or connection (e.g., links to<br>the next lesson/assessment; helps solve<br>real problems).</p></div>
  </section>

  <section class="track track-behaviour">
    <h2>BEHAVIOUR</h2>
    <div class="card card-what"><h4>WHAT</h4><p>The explicit behaviour expectation<br>(e.g., track the speaker; voice level;<br>hands/signals).</p></div>
    <div class="card card-how"><h4>HOW</h4><p>The routine to meet it (e.g., attention<br>signal → pause → response; partner roles;<br>“Ask 3 before me”).</p></div>
    <div class="card card-why"><h4>WHY</h4><p>Maximises learning time, safety, and<br>fairness for everyone.</p></div>
  </section>

  <div class="goal-tab"></div>
  <section class="goal-band"></section>
  <h2 class="goal-title">THE GOAL</h2>

  <svg class="flow-arrows" viewBox="0 0 570 168" aria-hidden="true">
    <g fill="var(--shadow)" transform="translate(2.5,2.5)">
      <path d="M101 62h10v18h7l-12 14-12-14h7z"/>
      <path d="M179 110h18v-7l15 12-15 12v-7h-18z"/>
      <path d="M280 97h10v-18h7l-12-14-12 14h7z"/>
      <path d="M357 39h18v-7l15 12-15 12v-7h-18z"/>
      <path d="M458 62h10v18h7l-12 14-12-14h7z"/>
    </g>
    <g fill="var(--yellow)">
      <path d="M101 62h10v18h7l-12 14-12-14h7z"/>
      <path d="M179 110h18v-7l15 12-15 12v-7h-18z"/>
      <path d="M280 97h10v-18h7l-12-14-12 14h7z"/>
      <path d="M357 39h18v-7l15 12-15 12v-7h-18z"/>
      <path d="M458 62h10v18h7l-12 14-12-14h7z"/>
    </g>
  </svg>

  <div class="step row-1 col-a">WARM UP<br>(ACTIVATE)</div>
  <div class="step row-1 col-b">YOU DO IT<br>TOGETHER</div>
  <div class="step row-1 col-c">YOU DO</div>
  <div class="step row-2 col-a">I DO</div>
  <div class="step row-2 col-b">WE DO</div>
  <div class="step row-2 col-c">REVIEW GOAL<br>&amp; SUCCESS CRITERIA</div>
</main>
</body>
</html>
```